Belle Rive Weddings and Events

I am a small boutique wedding coordinator, stylist and bridal consultant/coach/assistant. I am based in Brisbane, Australia and my business is geared towards mid range- high end budget bridal couples.
I am after some business cards that are double sided, with the logo on one side and all other information on the other side, including the business tagline of design, create, celebrate. The look of the card needs to be clean and crisp, with white and the tones of grey of the logo.The final design needs to convey sophistication and poise. Perhaps the logo and tagline could be done in a metallic silver with the rest of the text in the shades of grey from the style guide attached below.
Title- Mira Tolvarenko - Director / Events Manager and Stylist
Address - 218 Halbrook Terrace, Wexley Vale, QLD, 4127
Phone- 07 3894 2167
Mobile- 0438 725 519
Email- Mira@bellerivecelebra.com.au
Website- www.bellerivecelebra.com.au

```html
<!DOCTYPE html>
<html lang="en">
<head>
<meta charset="utf-8">
<title>Belle Rive Weddings and Events – Business Card Concepts</title>
<link href="https://fonts.googleapis.com/css2?family=Open+Sans:wght@300;400;700&family=Pinyon+Script&display=swap" rel="stylesheet">
<style>
  :root{
    --backdrop:#c9cdcf;
    --white:#f4f5f5;
    --paper:#e9ecec;
    --grey-light:#d4d8da;
    --grey-mid:#b3b8bb;
    --grey-dark:#8f9497;
    --ink:#6b7074;
    --silver:#a7acaf;
  }
  *{box-sizing:border-box;margin:0;padding:0}
  html,body{width:1200px;height:857px;overflow:hidden;background:var(--backdrop)}
  .sheet{position:relative;width:1200px;height:857px;font-family:"Open Sans",sans-serif}
  .card{position:absolute;width:256px;height:150px;overflow:hidden;box-shadow:0 2px 6px rgba(0,0,0,.18)}
  .card svg.shapes{position:absolute;inset:0;width:100%;height:100%}
  .ornament{position:absolute}
  .logo{position:absolute;right:22px;top:50%;transform:translateY(-50%);text-align:center;
        font-family:"Open Sans",sans-serif;font-weight:300;color:var(--silver);line-height:1.15}
  .logo .name{font-size:19px;display:block}
  .logo .sub{font-size:8px;letter-spacing:.5px;display:block}
  .details{position:absolute;font-size:6.4px;line-height:1.45}
  .details .person{font-family:"Pinyon Script",cursive;font-size:15px;line-height:1.2;display:block}
  .details .role{font-weight:700;display:block}
  .tagline-script{font-family:"Pinyon Script",cursive;font-size:9px;display:block;margin-top:3px}

  /* Concept 1 – waves */
  .c1-info{left:40px;top:140px;background:var(--grey-mid)}
  .c1-info .details{left:16px;top:24px;color:var(--white)}
  .c1-logo{left:304px;top:140px;background:var(--grey-light)}

  /* Concept 2 – angles */
  .c2-info{left:640px;top:140px;background:var(--grey-light)}
  .c2-info .tag{position:absolute;left:10px;top:10px;font-size:7px;line-height:1.25;color:var(--white);letter-spacing:1px;font-weight:700}
  .c2-info .emblem{position:absolute;left:14px;top:84px;width:30px;height:30px;border-radius:50%;background:var(--white)}
  .c2-info .person{position:absolute;left:52px;top:86px;font-size:13px;font-weight:700;color:var(--white)}
  .c2-info .role{position:absolute;left:52px;top:103px;font-size:6px;color:var(--white)}
  .c2-info .contact{position:absolute;left:14px;top:122px;font-size:5.6px;color:var(--white);line-height:1.5}
  .c2-logo{left:904px;top:140px;background:var(--white)}

  /* Concept 3 – stripes */
  .c3-info{left:40px;top:568px;background:var(--white)}
  .c3-info .details{left:0;right:0;top:22px;text-align:center;color:var(--ink)}
  .c3-logo{left:304px;top:568px;background:var(--white)}

  /* Concept 4 – damask */
  .c4-info{left:640px;top:568px;background:var(--grey-mid)}
  .c4-info .details{left:0;right:0;top:24px;text-align:center;color:var(--white)}
  .c4-logo{left:904px;top:568px;background:var(--white)}
</style>
</head>
<body>
<main class="sheet">

  <!-- Concept 1 -->
  <section class="card c1-info">
    <svg class="shapes" viewBox="0 0 256 150" preserveAspectRatio="none">
      <path d="M0 0H256V16C190 36 120 8 0 20Z" fill="var(--grey-dark)"/>
      <path d="M0 118C90 104 160 136 256 114V150H0Z" fill="var(--grey-dark)"/>
      <path d="M0 118C90 104 160 136 256 114" stroke="var(--white)" stroke-width="3" fill="none"/>
    </svg>
    <div class="ornament" role="img" aria-label="Soft floral swirl flourish" style="left:170px;top:60px;width:80px;height:55px;border-radius:40%;background:radial-gradient(var(--white),transparent 70%);opacity:.45"></div>
    <div class="details">
      <span class="person">Mira Tolvarenko</span>
      <span class="role">Director / Events Manager &amp; Stylist</span>
      218 Halbrook Terrace, Wexley Vale, QLD, 4127<br>
      07 3894 2167 | 0438 725 519<br>
      Mira@bellerivecelebra.com.au<br>
      www.bellerivecelebra.com.au<br>
      Design. Create. Celebrate
    </div>
  </section>
  <section class="card c1-logo">
    <svg class="shapes" viewBox="0 0 256 150" preserveAspectRatio="none">
      <path d="M0 118C80 90 170 140 256 104V150H0Z" fill="var(--grey-dark)"/>
      <path d="M0 118C80 90 170 140 256 104" stroke="var(--white)" stroke-width="3" fill="none"/>
    </svg>
    <div class="ornament" role="img" aria-label="Faint floral swirl flourish" style="left:14px;top:10px;width:90px;height:60px;border-radius:40%;background:radial-gradient(var(--white),transparent 70%);opacity:.6"></div>
    <div class="logo"><span class="name">Belle Rive</span><span class="sub">Weddings &amp; Events</span></div>
  </section>

  <!-- Concept 2 -->
  <section class="card c2-info">
    <svg class="shapes" viewBox="0 0 256 150" preserveAspectRatio="none">
      <path d="M0 0H120L90 40H0Z" fill="var(--white)" opacity=".55"/>
      <path d="M150 0H256V20L176 0Z" fill="var(--white)"/>
      <path d="M256 120V150H200Z" fill="var(--white)"/>
    </svg>
    <div class="tag">DESIGN<br>CREATE<br>CELEBRATE</div>
    <div class="emblem"></div>
    <div class="person">Mira Tolvarenko</div>
    <div class="role">Director | Events Manager &amp; Stylist</div>
    <div class="contact">
      07 3894 2167 | 0438 725 519 · 218 Halbrook Terrace, Wexley Vale, QLD, 4127<br>
      Mira@bellerivecelebra.com.au · www.bellerivecelebra.com.au
    </div>
  </section>
  <section class="card c2-logo">
    <svg class="shapes" viewBox="0 0 256 150" preserveAspectRatio="none">
      <path d="M0 0H70L0 50Z" fill="var(--grey-light)"/>
      <path d="M256 0V60L210 0Z" fill="var(--grey-light)"/>
      <path d="M256 150H170L256 90Z" fill="var(--grey-light)"/>
      <path d="M0 150V110L40 150Z" fill="var(--grey-light)"/>
    </svg>
    <div class="logo" style="right:60px"><span class="name">Belle Rive</span><span class="sub">Weddings &amp; Events</span></div>
  </section>

  <!-- Concept 3 -->
  <section class="card c3-info">
    <svg class="shapes" viewBox="0 0 256 150" preserveAspectRatio="none">
      <rect x="0" y="0" width="26" height="150" fill="var(--grey-light)"/>
      <rect x="6" y="0" width="4" height="150" fill="var(--white)"/>
      <rect x="15" y="0" width="4" height="150" fill="var(--white)"/>
      <rect x="230" y="0" width="26" height="150" fill="var(--grey-light)"/>
      <rect x="237" y="0" width="4" height="150" fill="var(--white)"/>
      <rect x="246" y="0" width="4" height="150" fill="var(--white)"/>
    </svg>
    <div class="ornament" role="img" aria-label="Scrolled flourish above the name" style="left:98px;top:10px;width:60px;height:10px;border-radius:5px;background:var(--grey-light)"></div>
    <div class="details">
      <span class="person">Mira Tolvarenko</span>
      <span class="role">Director / Events Manager &amp; Stylist</span>
      218 Halbrook Terrace, Wexley Vale, QLD, 4127<br>
      07 3894 2167 | 0438 725 519<br>
      Mira@bellerivecelebra.com.au<br>
      www.bellerivecelebra.com.au
      <span class="tagline-script">Design. Create. Celebrate</span>
    </div>
    <div class="ornament" role="img" aria-label="Scrolled flourish below the tagline" style="left:98px;top:132px;width:60px;height:8px;border-radius:4px;background:var(--grey-light)"></div>
  </section>
  <section class="card c3-logo">
    <svg class="shapes" viewBox="0 0 256 150" preserveAspectRatio="none">
      <rect x="0" y="0" width="30" height="150" fill="var(--grey-light)"/>
      <rect x="7" y="0" width="4" height="150" fill="var(--white)"/>
      <rect x="17" y="0" width="4" height="150" fill="var(--white)"/>
    </svg>
    <div class="logo" style="right:50px"><span class="name">Belle Rive</span><span class="sub">Weddings &amp; Events</span></div>
  </section>

  <!-- Concept 4 -->
  <section class="card c4-info">
    <div class="ornament" role="img" aria-label="Damask corner pattern" style="left:0;top:0;width:70px;height:60px;background:radial-gradient(circle at 0 0,var(--grey-light),transparent 75%)"></div>
    <div class="ornament" role="img" aria-label="Damask corner pattern" style="right:0;bottom:0;width:80px;height:70px;background:radial-gradient(circle at 100% 100%,var(--grey-light),transparent 75%)"></div>
    <div class="details">
      <span class="person">Mira Tolvarenko</span>
      <span class="role">Director / Events Manager &amp; Stylist</span>
      218 Halbrook Terrace, Wexley Vale, QLD, 4127<br>
      07 3894 2167 | 0438 725 519<br>
      Mira@bellerivecelebra.com.au<br>
      www.bellerivecelebra.com.au
      <span class="tagline-script">Design. Create. Celebrate</span>
    </div>
  </section>
  <section class="card c4-logo">
    <div class="ornament" role="img" aria-label="Damask corner pattern" style="right:0;top:0;width:80px;height:70px;background:radial-gradient(circle at 100% 0,var(--grey-light),transparent 75%)"></div>
    <div class="ornament" role="img" aria-label="Damask corner pattern" style="right:0;bottom:0;width:90px;height:70px;background:radial-gradient(circle at 100% 100%,var(--grey-light),transparent 75%)"></div>
    <div class="logo" style="right:70px"><span class="name">Belle Rive</span><span class="sub">Weddings &amp; Events</span></div>
  </section>

</main>
</body>
</html>
```